Wine label for South African wine

modern, creative wine label name: Vaalbrook The Marivel-Trade GmbH - Sundry Vintners one of the leading independent providers of inexpensive wines from around the world. The company focuses entirely on this dynamic, constantly evolving wine market, and our customers can therefore take full advantage of a complete supply chain management for themselves, including: * http://www.marivelhandel.de/img/blatt.jpg procuring wines from the major producing regions around the globe * logistics and processing * wage filling and packaging * dealcoholization of wines for gastronomic purposes * design of exclusive client and proprietary brands, the target market / target group: the International market design Features; Modern, simple, meaningful, unique; Colors: gold, black, red;

Target Market(s)

Off Trade

Industry/Entity Type

Union

Font styles to use
Serif
Script

Requirements
Must have
• Modern, simple, meaningful, unique colors: gold, black, red varieties: Cab Sauv, Chard, Chenin, Merlot, Merlot Rose, Pinotage, Pinotage Rose, Shiraz, Red, Rose, White Non transparent max. Size: 12 x 9 cm data on VE: name brand, variety, country; WITHOUT Year

```html
<!DOCTYPE html>
<html lang="en">
<head>
<meta charset="utf-8">
<title>Vaalbrook – Cab Sauv Wine Label</title>
<link rel="stylesheet" href="https://fonts.googleapis.com/css2?family=Cormorant+Garamond:wght@500&family=Pinyon+Script&display=swap">
<style>
  :root {
    --page-bg: #ffffff;
    --label-bg: #ffffff;
    --label-border: #b9b9b9;
    --ink-black: #1a1a1a;
    --gold: #b8912e;
    --gold-light: #d4b35a;
    --wine-red: #c0141c;
  }
  * { margin: 0; padding: 0; box-sizing: border-box; }
  html, body {
    width: 1200px;
    height: 600px;
    overflow: hidden;
    background: var(--page-bg);
  }
  .canvas {
    position: relative;
    width: 1200px;
    height: 600px;
  }
  .wine-label {
    position: absolute;
    left: 386px;
    top: 10px;
    width: 426px;
    height: 580px;
    background: var(--label-bg);
    border: 1px solid var(--label-border);
  }
  .emblem {
    position: absolute;
    left: 149px;
    top: 14px;
    width: 128px;
    height: 190px;
  }
  .variety-name {
    position: absolute;
    left: 0;
    right: 0;
    top: 252px;
    text-align: center;
    font-family: "Cormorant Garamond", "Times New Roman", serif;
    font-weight: 500;
    font-size: 60px;
    line-height: 1;
    letter-spacing: 2px;
    color: var(--ink-black);
  }
  .gold-rule {
    position: absolute;
    left: 100px;
    width: 226px;
    top: 362px;
    height: 2px;
    background: var(--gold);
  }
  .region {
    position: absolute;
    left: 0;
    right: 0;
    top: 403px;
    text-align: center;
    font-family: "Cormorant Garamond", "Times New Roman", serif;
    font-weight: 500;
    font-size: 21px;
    letter-spacing: 1px;
    color: var(--ink-black);
  }
  .country {
    position: absolute;
    left: 0;
    right: 0;
    top: 496px;
    text-align: center;
    font-family: "Pinyon Script", cursive;
    font-size: 28px;
    color: var(--wine-red);
  }
</style>
</head>
<body>
  <main class="canvas">
    <section class="wine-label">
      <svg class="emblem" viewBox="0 0 128 190" role="img" aria-label="Gold lion head emblem holding a door-knocker ring">
        <defs>
          <radialGradient id="emblemGold" cx="50%" cy="45%" r="60%">
            <stop offset="0%" stop-color="#d4b35a"/>
            <stop offset="100%" stop-color="#b8912e"/>
          </radialGradient>
        </defs>
        <rect x="0" y="0" width="128" height="190" rx="50" fill="url(#emblemGold)"/>
      </svg>
      <h1 class="variety-name">CAB SAUV</h1>
      <div class="gold-rule"></div>
      <p class="region">WESTERN CAPE</p>
      <p class="country">South Africa</p>
    </section>
  </main>
</body>
</html>
```